BRIMWAVE.live*

I am needing a web site built for the main purpose of uploading podcasts
(MP3 files) to be viewed by large audiences of 1000+ site visitors on a regular basis. I have created a rough draft of how I want the site to look.

i have created a rough draft of the home page - the LOGO for this site is a spectacular lightening bolt which appears on my home page sample... the file for this image I purchased is too large to download to your site. I will supply on reuquest.

There will be 5 pages; HOME ABOUT RESOURCES DEVOTIONALS MORTY.
I have all the content prepared for each of the above pages.

Target Market(s)

All people groups seeking positive and encouraging words, life lessons and testimonies of faith.

Coding

Coded - Design and coding required

Number of Pages Required

1 page

Colors
3176b5

Requirements
Must have
• The design and layout provided - my sample

Black backgrounds as shown on my sample

```html
<!DOCTYPE html>
<html lang="en">
<head>
<meta charset="utf-8">
<title>BRIMWAVE.live – Life Changing Podcasts</title>
<link rel="stylesheet" href="https://fonts.googleapis.com/css2?family=Abril+Fatface&family=Lato:wght@400&display=swap">
<style>
  :root {
    --brand-blue: #3176b5;
    --night: #020a2e;
    --deep: #0a2c8a;
    --glow: #1e64e0;
    --white: #ffffff;
    --footer: #070a07;
    --ring: #c8262c;
  }
  * { margin: 0; padding: 0; box-sizing: border-box; }
  html, body { width: 1200px; height: 1092px; overflow: hidden; background: var(--footer); }
  .page { position: relative; width: 1200px; height: 1092px; overflow: hidden; }

  .hero {
    position: absolute; left: 0; top: 0; width: 1200px; height: 1014px;
    background:
      radial-gradient(ellipse 420px 520px at 700px 520px, rgba(0,220,255,0.35), transparent 70%),
      radial-gradient(ellipse 700px 650px at 560px 480px, var(--glow), var(--deep) 55%, var(--night) 100%);
  }
  .hero-portrait {
    position: absolute; left: 34px; top: 107px; width: 579px; height: 791px;
    background: linear-gradient(180deg, #7a6a5c 0%, #3a302c 35%, #141414 60%, #0d0d0d 100%);
    border-radius: 180px 180px 20px 20px;
  }

  .site-nav {
    position: absolute; left: 0; top: 18px; width: 1200px; height: 46px;
    font-family: 'Abril Fatface', serif; color: var(--white);
  }
  .nav-link { position: absolute; top: 14px; font-size: 15px; letter-spacing: 0.3px; }
  .brand {
    position: absolute; left: 415px; top: 0; width: 368px; text-align: center;
    font-size: 40px; line-height: 46px; letter-spacing: 1px;
  }

  .headline {
    position: absolute; left: 700px; width: 480px; text-align: center;
    font-family: 'Abril Fatface', serif; color: var(--white);
    font-size: 64px; line-height: 64px; letter-spacing: 2px;
  }

  .episodes { position: absolute; left: 0; top: 898px; width: 1200px; height: 116px; }
  .episode {
    position: absolute; top: 0; width: 236px; height: 116px;
    background: var(--brand-blue); color: var(--white); text-align: center;
  }
  .episode-icon { position: absolute; left: 98px; top: -20px; }
  .episode-title {
    position: absolute; left: 0; top: 30px; width: 100%;
    font-family: 'Abril Fatface', serif; font-size: 17px; letter-spacing: 0.5px;
  }
  .episode-text {
    position: absolute; left: 0; top: 60px; width: 100%;
    font-family: Arial, Helvetica, sans-serif; font-size: 13px; line-height: 23px;
  }

  .site-footer {
    position: absolute; left: 0; top: 1014px; width: 1200px; height: 78px; background: var(--footer);
    color: var(--white);
  }
  .copyright {
    position: absolute; left: 114px; top: 30px;
    font-family: 'Lato', sans-serif; font-size: 15px;
  }
  .social { position: absolute; left: 956px; top: 28px; display: flex; gap: 7px; }
  .social-item {
    width: 27px; height: 27px; border: 1px solid var(--white); border-radius: 50%;
    font-family: 'Lato', sans-serif; font-size: 8px; line-height: 25px; text-align: center;
  }
</style>
</head>
<body>
<div class="page">
  <section class="hero" role="img" aria-label="Deep blue backdrop with a glowing cyan lightning bolt and outline shapes">
    <div class="hero-portrait" role="img" aria-label="Photo of the host in a black t-shirt with arms crossed"></div>
  </section>

  <nav class="site-nav">
    <span class="nav-link" style="left:128px">HOME</span>
    <span class="nav-link" style="left:225px">ABOUT</span>
    <span class="nav-link" style="left:328px">MORTY</span>
    <span class="brand">BRIMWAVE.live</span>
    <span class="nav-link" style="left:814px">RESOURCES</span>
    <span class="nav-link" style="left:961px">DEVOTIONALS</span>
  </nav>

  <h1>
    <span class="headline" style="top:330px">LIFE</span>
    <span class="headline" style="top:486px">CHANGING</span>
    <span class="headline" style="top:642px">PODCASTS</span>
  </h1>

  <section class="episodes">
    <article class="episode" style="left:0">
      <svg class="episode-icon" width="40" height="40" viewBox="0 0 40 40"><circle cx="20" cy="20" r="19" fill="var(--ring)"/><circle cx="20" cy="21" r="17" fill="var(--brand-blue)" stroke="#fff" stroke-width="2"/></svg>
      <h2 class="episode-title">Episode -1</h2>
      <p class="episode-text">Lorem ipsum dolor sit amet, ctetur<br>adipiscing elit, sed do eiusmod</p>
    </article>
    <article class="episode" style="left:241px">
      <svg class="episode-icon" width="40" height="40" viewBox="0 0 40 40"><circle cx="20" cy="20" r="19" fill="var(--ring)"/><circle cx="20" cy="21" r="17" fill="var(--brand-blue)" stroke="#fff" stroke-width="2"/></svg>
      <h2 class="episode-title">Episode -2</h2>
      <p class="episode-text">Lorem ipsum dolor sit amet, ctetur<br>adipiscing elit, sed do eiusmod</p>
    </article>
    <article class="episode" style="left:482px">
      <svg class="episode-icon" width="40" height="40" viewBox="0 0 40 40"><circle cx="20" cy="20" r="19" fill="var(--ring)"/><circle cx="20" cy="21" r="17" fill="var(--brand-blue)" stroke="#fff" stroke-width="2"/></svg>
      <h2 class="episode-title">Episode -3</h2>
      <p class="episode-text">Lorem ipsum dolor sit amet, ctetur<br>adipiscing elit, sed do eiusmod</p>
    </article>
    <article class="episode" style="left:723px">
      <svg class="episode-icon" width="40" height="40" viewBox="0 0 40 40"><circle cx="20" cy="20" r="19" fill="var(--ring)"/><circle cx="20" cy="21" r="17" fill="var(--brand-blue)" stroke="#fff" stroke-width="2"/></svg>
      <h2 class="episode-title">Episode -4</h2>
      <p class="episode-text">Lorem ipsum dolor sit amet, ctetur<br>adipiscing elit, sed do eiusmod</p>
    </article>
    <article class="episode" style="left:964px">
      <svg class="episode-icon" width="40" height="40" viewBox="0 0 40 40"><circle cx="20" cy="20" r="19" fill="var(--ring)"/><circle cx="20" cy="21" r="17" fill="var(--brand-blue)" stroke="#fff" stroke-width="2"/></svg>
      <h2 class="episode-title">Episode -5</h2>
      <p class="episode-text">Lorem ipsum dolor sit amet, ctetur<br>adipiscing elit, sed do eiusmod</p>
    </article>
  </section>

  <footer class="site-footer">
    <p class="copyright">Copyright © 2020 BRIMWAVE.live. All Rights Reserved.</p>
    <div class="social">
      <span class="social-item">Pal</span>
      <span class="social-item">Pix</span>
      <span class="social-item">Tok</span>
      <span class="social-item">Net</span>
    </div>
  </footer>
</div>
</body>
</html>
```